website re-design

require to re design my existing website ( www.lunarfoxgrove.example ) to show a corporate image of the company . i also require an advise on the content editorial text . i am currently using pel wimbo for domain registration and website design and publishing .

Target Market(s)

focus on the meddle east market , but visible for worldwide business opportunity

Industry/Entity Type

It Company

Coding

Coded - Design and coding required

Number of Pages Required

5+ page

Requirements
Must have
• --show the brand color when possible ,
• --professional website reflecting the following main key areas :broadcast /media/consultancy services/technology
• --number of pages to be maintained or increased if necessary
• --adaptive design for all PC and mobiles
• --simple to navigate and get the idea quickly
• --landing page with full image and slight movement in the background
Nice to have
• any interactivity with visitors
• font style to be recommended by the designer ( professional test , easy to read )
• more descriptive image and less text
• visitor to know what we do more from graphics , image and video
• landing page to have some motions ( similar to www.harbortwillco.example/ )

```html
<!DOCTYPE html>
<html lang="en">
<head>
<meta charset="utf-8">
<title>Lunar Fox Grove — Broadcast System Solutions</title>
<link href="https://fonts.googleapis.com/css2?family=Open+Sans:wght@400;600;700&display=swap" rel="stylesheet">
<style>
  :root{
    --brand:#ef6c0c;
    --ink:#111111;
    --nav-bg:#1c1916;
    --peach:#fde4d4;
    --card:#fbeee4;
    --muted:#6a6a6a;
    --rule:#c9c2bc;
    --gold-rule:#e3b77f;
    --white:#ffffff;
  }
  *{box-sizing:border-box;margin:0;padding:0}
  html,body{width:929px;height:1200px;overflow:hidden}
  body{position:relative;background:var(--peach);font-family:"Open Sans",Arial,sans-serif;color:var(--ink)}

  .site-nav{position:absolute;left:0;top:0;width:929px;height:56px;background:var(--nav-bg);z-index:3}
  .brand-mark{position:absolute;left:64px;top:0;width:96px;height:91px;background:var(--brand);z-index:4;
    color:var(--white);font-weight:400;font-size:16px;line-height:16px;padding:34px 0 0 9px;letter-spacing:-.2px}
  .nav-links{position:absolute;top:17px;left:0;list-style:none}
  .nav-links li{position:absolute;top:0;height:23px;line-height:23px;font-size:10.5px;font-weight:600;color:var(--white);white-space:nowrap}
  .nav-links li.active{background:var(--brand);width:56px;text-align:center}

  .hero{position:absolute;left:0;top:56px;width:929px;height:585px;
    background:
      radial-gradient(ellipse 320px 200px at 455px 300px,#fff6c8 0%,#ffe07a 30%,rgba(255,180,90,0) 75%),
      linear-gradient(180deg,#b99ac4 0%,#e2a7c4 20%,#f7c3a6 42%,#f6b262 62%,#a5552a 80%,#3a1d12 100%)}

  .content-panel{position:absolute;left:71px;top:416px;width:792px;height:770px;background:var(--white)}

  .intro-title{position:absolute;left:0;top:438px;width:929px;text-align:center;font-size:23px;font-weight:700;letter-spacing:.3px}
  .intro-title span{color:var(--brand)}
  .intro-rule{position:absolute;left:298px;top:470px;width:353px;height:1px;background:var(--rule)}
  .intro-copy{position:absolute;left:118px;top:482px;width:700px;font-size:12.4px;line-height:19.5px}

  .service{position:absolute;top:574px;width:222px}
  .service .photo{height:131px}
  .service p{margin-top:10px;text-align:center;font-size:11.5px;line-height:15px}
  .service.featured p{color:var(--brand)}

  .section-title{position:absolute;top:790px;font-size:19px;font-weight:700;letter-spacing:.2px}
  .section-title span{color:var(--brand)}
  .section-rule{position:absolute;top:816px;height:1px}

  .news-card{position:absolute;left:112px;width:346px;height:102px;background:var(--card);padding:8px 8px 0 7px}
  .news-card h3{font-size:11.8px;font-weight:400;line-height:16px}
  .news-card p{margin-top:4px;font-size:11.4px;line-height:14.5px;color:var(--muted);text-align:justify}
  .news-card time{position:absolute;left:9px;bottom:6px;font-size:8.5px;color:var(--muted)}

  .client{position:absolute;width:100px;margin-left:-50px;text-align:center;font-size:15px;font-weight:600;color:#2d2d2d;line-height:18px}

  .chat-widget{position:absolute;left:722px;top:1157px;width:194px;height:29px;background:var(--brand);color:var(--white);
    font-size:12px;line-height:29px;padding-left:45px;border-radius:2px 2px 0 0}
  .chat-widget svg{position:absolute}
  .chat-divider{position:absolute;left:30px;top:0;width:1px;height:29px;background:rgba(255,255,255,.35)}

  .footer-band{position:absolute;left:0;top:1186px;width:929px;height:14px;background:var(--ink)}
</style>
</head>
<body>

<header class="site-nav">
  <ul class="nav-links">
    <li class="active" style="left:420px">Home</li>
    <li style="left:491px">About</li>
    <li style="left:543px">Services</li>
    <li style="left:606px">Solutions</li>
    <li style="left:675px">Customer</li>
    <li style="left:744px">Employment</li>
    <li style="left:827px">Contact</li>
  </ul>
</header>
<div class="brand-mark">LUNAR<br>FOX<br>GROVE</div>

<div class="hero" role="img" aria-label="Photo of a telecom tower with dish antennas silhouetted against a sunset sky over mountains"></div>

<main class="content-panel"></main>

<h1 class="intro-title"><span>LUNAR FOX</span> GROVE</h1>
<div class="intro-rule"></div>
<p class="intro-copy">Lunar Fox Grove Provides Broadcast System Solutions and Services to support broadcasters , production house, telecom and satellite operator to achieve their goals of media innovation and operation efficiency through strategic planning and smart investment relying on innovative technologies&nbsp; solutions and professional Services .</p>

<section class="service featured" style="left:119px">
  <div class="photo" role="img" aria-label="Photo of business consultants reviewing a tablet" style="background:linear-gradient(160deg,#e9eef4 0%,#5a6f92 45%,#1d2c4d 70%,#dfe6ee 100%)"></div>
  <p>Consultancy and Project<br>Management</p>
</section>
<section class="service" style="left:355px">
  <div class="photo" role="img" aria-label="Photo of a hand using a tablet with a digital globe overlay" style="background:linear-gradient(135deg,#0f2a3c 0%,#2f7c9e 45%,#9fc7d6 60%,#173848 100%)"></div>
  <p>Engineering and Managed<br>Services</p>
</section>
<section class="service" style="left:590px">
  <div class="photo" role="img" aria-label="Photo of network cables plugged into a patch panel" style="background:linear-gradient(170deg,#1d3b60 0%,#b0323b 30%,#2f69a8 50%,#7fa2b0 75%,#3d4c55 100%)"></div>
  <p>Innovative Broadcast<br>Technology solutions</p>
</section>

<h2 class="section-title" style="left:118px"><span>UPDATED</span> NEWS</h2>
<div class="section-rule" style="left:118px;width:338px;background:var(--rule)"></div>
<h2 class="section-title" style="left:522px">CUSTOMER</h2>
<div class="section-rule" style="left:517px;width:338px;background:var(--gold-rule)"></div>

<article class="news-card" style="top:829px">
  <h3>Brightmesh Does 20 Gbps Millimeter-Wave Broadband</h3>
  <p>The radio frequency folks at Brightmesh say they've achieved a data rate of 20 Gbps over millimeter-wave technology at a distance ...</p>
  <time>11/12/2016, 3:32:00 AM</time>
</article>
<article class="news-card" style="top:943px">
  <h3>Watch Now: TRSA Publishes Video on Anchor Corrosion</h3>
  <p>The Tower Rigging Safety Alliance has published a video showing how tower anchors corrode and ways to protect them.</p>
  <time>11/12/2016, 3:32:00 AM</time>
</article>
<article class="news-card" style="top:1057px">
  <h3>Brightmesh Does 20 Gbps Millimeter-Wave Broadband</h3>
  <p>The radio frequency folks at Brightmesh say they've achieved a data rate of 20 Gbps over millimeter-wave technology at a distance ...</p>
  <time>11/12/2016, 3:32:00 AM</time>
</article>

<div class="client" style="left:556px;top:845px">Kestran</div>
<div class="client" style="left:663px;top:845px">novalink</div>
<div class="client" style="left:770px;top:836px">Quayside Studios</div>
<div class="client" style="left:556px;top:940px">Radio 96.3</div>
<div class="client" style="left:663px;top:940px">skyrelay</div>
<div class="client" style="left:770px;top:940px">Nour TV</div>
<div class="client" style="left:556px;top:1025px">Meridian Advisors</div>
<div class="client" style="left:663px;top:1034px">Zone Eleven</div>
<div class="client" style="left:770px;top:1025px">Civic Works Board</div>

<aside class="chat-widget">
  <svg style="left:9px;top:9px" width="13" height="10" viewBox="0 0 13 10" aria-hidden="true">
    <rect x=".75" y=".75" width="11.5" height="8.5" fill="none" stroke="#fff" stroke-width="1.5"/>
    <path d="M1 1l5.5 4.5L12 1" fill="none" stroke="#fff" stroke-width="1.5"/>
  </svg>
  <span class="chat-divider"></span>
  Leave a message
  <svg style="right:10px;top:12px" width="9" height="6" viewBox="0 0 9 6" aria-hidden="true">
    <path d="M1 5l3.5-3.5L8 5" fill="none" stroke="#fff" stroke-width="1.6"/>
  </svg>
</aside>

<footer class="footer-band"></footer>

</body>
</html>
```